Securities Exam Training Banner Add for Adlane campaign

We need a banner ad design to use for a remarketing campaign in Brixel Adlane. We are a securities exam training provider that provides online training across the U.S. and Canada. Banner ad designs should be consistent in color and concept with our website: www.vornapreplabs.example.

Approved ad copy:

"Pass on your first attempt. Experience what you are missing with your current training provider."

"Pass the Tier 4 on your first attempt with our industry-leading training program. "

-High quality audio lecture.
-Interactive visual presentations.
-Comprehensive course textbook.

"We give you everything you need to pass on your first attempt."

Deliverables:

-Ad Sizes (250x250; 200x200; 468x60; 728x90; 300x250; 336x280; 120x600; 160x600)
-.gif, .jpg, .png, or .swf
-50kb or smaller

Theme:

-Design should reflect financial security, confidence in the product, and differentiation from the "rest of the industry."

Target Market(s)

People who are training for securities exams in the financial industry. e.g. people who work for Halberd Quint, Dorsey Pellham, Ashby Crane, etc..

Industry/Entity Type

Financial

Requirements
Must have
• Company Logo and phrase "The leader in securities exam prep"
Strong call to action on final screen (Buy Now).

```html
<!DOCTYPE html>
<html lang="en">
<head>
<meta charset="utf-8">
<title>Vorna Prep Labs – Banner Set</title>
<link rel="stylesheet" href="https://fonts.googleapis.com/css2?family=Antonio:wght@700&family=Lato:wght@400;700&display=swap">
<style>
  :root {
    --stage: #3b3a38;
    --blue-deep: #0b3f9c;
    --blue-mid: #1c5dc6;
    --blue-light: #3d7fe0;
    --band: #1f64d0;
    --white: #ffffff;
    --silver-top: #ffffff;
    --silver-bottom: #b9c3cf;
    --tick: #f3c623;
    --logo-grey: #5a6068;
    --logo-mark: #2f5fa8;
    --btn-top: #ffd64a;
    --btn-bottom: #f5a000;
    --btn-text: #1d1d1d;
    --btn-edge: #d48800;
    --photo-a: #b9c4d6;
    --photo-b: #2b2d33;
  }
  * { box-sizing: border-box; margin: 0; padding: 0; }
  html, body { width: 1200px; height: 870px; overflow: hidden; }
  body { background: var(--stage); position: relative; font-family: "Lato", Arial, sans-serif; }

  .banner { position: absolute; overflow: hidden; background: var(--white); }
  .banner__field {
    position: absolute; left: 0; top: 0;
    background: linear-gradient(160deg, var(--blue-light) 0%, var(--blue-mid) 40%, var(--blue-deep) 100%);
  }
  .banner__field::after {
    content: ""; position: absolute; left: 0; right: 0; bottom: 0; height: 6px; background: var(--band);
  }
  .headline {
    position: absolute; font-family: "Antonio", "Arial Narrow", sans-serif; font-weight: 700;
    text-transform: uppercase; letter-spacing: 0; white-space: nowrap;
    background: linear-gradient(180deg, var(--silver-top) 30%, var(--silver-bottom) 100%);
    -webkit-background-clip: text; background-clip: text; color: transparent;
    filter: drop-shadow(1px 2px 1px rgba(0,0,0,.45));
  }
  .headline span { display: block; }
  .features { position: absolute; list-style: none; color: var(--white); }
  .features li { position: relative; padding-left: 1.15em; }
  .features li::before {
    content: "✓"; position: absolute; left: 0; top: 0; color: var(--tick); font-weight: 700;
  }
  .photo {
    position: absolute;
    background: radial-gradient(ellipse at 50% 30%, var(--photo-a) 0%, #7f8ea8 35%, var(--photo-b) 80%);
  }
  .notch {
    position: absolute; width: 0; height: 0;
    border-left: 9px solid transparent; border-right: 9px solid transparent;
    border-bottom: 11px solid var(--white);
  }
  .logo { position: absolute; display: flex; align-items: center; gap: 7px; }
  .logo__mark { background: var(--logo-mark); flex: none; }
  .logo__name {
    color: var(--logo-grey); font-family: "Lato", Arial, sans-serif; font-weight: 400;
    text-transform: uppercase; line-height: 1; white-space: nowrap;
  }
  .buy {
    position: absolute; display: flex; align-items: center; justify-content: center; gap: 10px;
    background: linear-gradient(180deg, var(--btn-top) 0%, var(--btn-bottom) 100%);
    border: 1px solid var(--btn-edge); border-radius: 5px;
    box-shadow: 0 2px 3px rgba(0,0,0,.35);
    color: var(--btn-text); font-family: "Lato", Arial, sans-serif; font-weight: 700;
  }
  .buy svg { flex: none; }

  /* 160x600 skyscraper */
  .sky { left: 29px; top: 93px; width: 198px; height: 745px; }
  .sky .banner__field { width: 198px; height: 617px; }
  .sky .headline { left: 0; width: 198px; text-align: center; top: 18px; font-size: 36px; line-height: 42px; }
  .sky .features { left: 10px; top: 170px; font-size: 19px; line-height: 22px; width: 170px; }
  .sky .features li { margin-bottom: 14px; }
  .sky .photo { left: 0; top: 360px; width: 198px; height: 257px; }
  .sky .notch { left: 14px; top: 607px; }
  .sky .logo { left: 14px; top: 636px; }
  .sky .logo__mark { width: 32px; height: 32px; }
  .sky .logo__name { font-size: 16px; }
  .sky .buy { left: 9px; top: 685px; width: 177px; height: 46px; font-size: 22px; }

  /* 336x280 medium rectangle */
  .rect { left: 248px; top: 190px; width: 417px; height: 347px; }
  .rect .banner__field { width: 417px; height: 279px; }
  .rect .headline { left: 0; width: 265px; text-align: center; top: 10px; font-size: 40px; line-height: 46px; }
  .rect .features { left: 14px; top: 170px; font-size: 18px; line-height: 28px; white-space: nowrap; }
  .rect .photo { left: 265px; top: 9px; width: 152px; height: 270px; }
  .rect .notch { left: 14px; top: 269px; }
  .rect .logo { left: 14px; top: 292px; }
  .rect .logo__mark { width: 34px; height: 34px; }
  .rect .logo__name { font-size: 19px; }
  .rect .buy { left: 223px; top: 292px; width: 177px; height: 44px; font-size: 22px; }

  /* 300x250 square */
  .square { left: 700px; top: 190px; width: 372px; height: 310px; }
  .square .banner__field { width: 372px; height: 244px; }
  .square .headline { left: 0; width: 240px; text-align: center; top: 8px; font-size: 36px; line-height: 42px; }
  .square .features { left: 12px; top: 150px; font-size: 16px; line-height: 26px; white-space: nowrap; }
  .square .photo { left: 240px; top: 8px; width: 132px; height: 236px; }
  .square .notch { left: 14px; top: 234px; }
  .square .logo { left: 12px; top: 259px; }
  .square .logo__mark { width: 30px; height: 30px; }
  .square .logo__name { font-size: 17px; }
  .square .buy { left: 200px; top: 258px; width: 157px; height: 41px; font-size: 20px; }

  /* 468x60 banner */
  .small { left: 272px; top: 571px; width: 581px; height: 72px; }
  .small .banner__field { width: 403px; height: 72px; }
  .small .banner__field::after { display: none; }
  .small .headline { left: 0; width: 186px; text-align: center; top: 6px; }
  .small .headline .line-a { font-size: 27px; line-height: 31px; }
  .small .headline .line-b { font-size: 20px; line-height: 28px; }
  .small .divider { position: absolute; left: 188px; top: 6px; width: 1px; height: 60px; background: rgba(255,255,255,.35); }
  .small .features { left: 194px; top: 6px; font-size: 11.5px; line-height: 20px; white-space: nowrap; }
  .small .photo { left: 522px; top: 0; width: 59px; height: 72px; }
  .small .logo { left: 415px; top: 7px; gap: 5px; }
  .small .logo__mark { width: 20px; height: 20px; }
  .small .logo__name { font-size: 11px; }
  .small .buy { left: 415px; top: 35px; width: 97px; height: 27px; font-size: 13px; gap: 6px; border-radius: 4px; }

  /* 728x90 leaderboard */
  .board { left: 248px; top: 668px; width: 904px; height: 111px; }
  .board .banner__field { width: 627px; height: 111px; }
  .board .banner__field::after { display: none; }
  .board .headline { left: 0; width: 296px; text-align: center; top: 8px; }
  .board .headline .line-a { font-size: 46px; line-height: 52px; }
  .board .headline .line-b { font-size: 31px; line-height: 40px; }
  .board .divider { position: absolute; left: 298px; top: 10px; width: 1px; height: 91px; background: rgba(255,255,255,.35); }
  .board .features { left: 305px; top: 9px; font-size: 19px; line-height: 31px; white-space: nowrap; }
  .board .notch { left: 616px; top: 47px; border-left: 0; border-top: 9px solid transparent; border-bottom: 9px solid transparent; border-right: 11px solid var(--white); }
  .board .photo { left: 818px; top: 0; width: 86px; height: 111px; }
  .board .logo { left: 648px; top: 12px; }
  .board .logo__mark { width: 30px; height: 30px; }
  .board .logo__name { font-size: 17px; }
  .board .buy { left: 646px; top: 56px; width: 155px; height: 41px; font-size: 21px; }
</style>
</head>
<body>

<!-- 160x600 skyscraper -->
<section class="banner sky" aria-label="Skyscraper banner">
  <div class="banner__field"></div>
  <h2 class="headline"><span>The leader</span><span>in securities</span><span>exam prep</span></h2>
  <ul class="features">
    <li>High quality audio lecture.</li>
    <li>Interactive visual presentations.</li>
    <li>Comprehensive course textbook.</li>
  </ul>
  <div class="photo" role="img" aria-label="Photo of a smiling professional woman in glasses and a dark business suit"></div>
  <div class="notch"></div>
  <div class="logo"><span class="logo__mark"></span><span class="logo__name">Vorna<br>Prep Labs</span></div>
  <a class="buy">Buy Now
    <svg width="26" height="26" viewBox="0 0 26 26"><circle cx="13" cy="13" r="12" fill="#fff"/><path d="M10.5 7.5 L16 13 L10.5 18.5" fill="none" stroke="#222" stroke-width="3" stroke-linecap="round" stroke-linejoin="round"/></svg>
  </a>
</section>

<!-- 336x280 medium rectangle -->
<section class="banner rect" aria-label="Medium rectangle banner">
  <div class="banner__field"></div>
  <div class="photo" role="img" aria-label="Photo of a smiling professional woman in glasses and a dark business suit"></div>
  <h2 class="headline"><span>The leader</span><span>in securities</span><span>exam prep</span></h2>
  <ul class="features">
    <li>High quality audio lecture.</li>
    <li>Interactive visual presentations.</li>
    <li>Comprehensive course textbook.</li>
  </ul>
  <div class="notch"></div>
  <div class="logo"><span class="logo__mark"></span><span class="logo__name">Vorna<br>Prep Labs</span></div>
  <a class="buy">Buy Now
    <svg width="26" height="26" viewBox="0 0 26 26"><circle cx="13" cy="13" r="12" fill="#fff"/><path d="M10.5 7.5 L16 13 L10.5 18.5" fill="none" stroke="#222" stroke-width="3" stroke-linecap="round" stroke-linejoin="round"/></svg>
  </a>
</section>

<!-- 300x250 square -->
<section class="banner square" aria-label="Square banner">
  <div class="banner__field"></div>
  <div class="photo" role="img" aria-label="Photo of a smiling professional woman in glasses and a dark business suit"></div>
  <h2 class="headline"><span>The leader</span><span>in securities</span><span>exam prep</span></h2>
  <ul class="features">
    <li>High quality audio lecture.</li>
    <li>Interactive visual presentations.</li>
    <li>Comprehensive course textbook.</li>
  </ul>
  <div class="notch"></div>
  <div class="logo"><span class="logo__mark"></span><span class="logo__name">Vorna<br>Prep Labs</span></div>
  <a class="buy">Buy Now
    <svg width="24" height="24" viewBox="0 0 26 26"><circle cx="13" cy="13" r="12" fill="#fff"/><path d="M10.5 7.5 L16 13 L10.5 18.5" fill="none" stroke="#222" stroke-width="3" stroke-linecap="round" stroke-linejoin="round"/></svg>
  </a>
</section>

<!-- 468x60 banner -->
<section class="banner small" aria-label="Full banner">
  <div class="banner__field"></div>
  <h2 class="headline"><span class="line-a">The leader in</span><span class="line-b">securities exam prep</span></h2>
  <div class="divider"></div>
  <ul class="features">
    <li>High quality audio lecture.</li>
    <li>Interactive visual presentations.</li>
    <li>Comprehensive course textbook.</li>
  </ul>
  <div class="logo"><span class="logo__mark"></span><span class="logo__name">Vorna<br>Prep Labs</span></div>
  <a class="buy">Buy Now
    <svg width="16" height="16" viewBox="0 0 26 26"><circle cx="13" cy="13" r="12" fill="#fff"/><path d="M10.5 7.5 L16 13 L10.5 18.5" fill="none" stroke="#222" stroke-width="3.5" stroke-linecap="round" stroke-linejoin="round"/></svg>
  </a>
  <div class="photo" role="img" aria-label="Photo of a smiling professional woman in glasses and a dark business suit"></div>
</section>

<!-- 728x90 leaderboard -->
<section class="banner board" aria-label="Leaderboard banner">
  <div class="banner__field"></div>
  <h2 class="headline"><span class="line-a">The leader in</span><span class="line-b">securities exam prep</span></h2>
  <div class="divider"></div>
  <ul class="features">
    <li>High quality audio lecture.</li>
    <li>Interactive visual presentations.</li>
    <li>Comprehensive course textbook.</li>
  </ul>
  <div class="notch"></div>
  <div class="logo"><span class="logo__mark"></span><span class="logo__name">Vorna<br>Prep Labs</span></div>
  <a class="buy">Buy Now
    <svg width="25" height="25" viewBox="0 0 26 26"><circle cx="13" cy="13" r="12" fill="#fff"/><path d="M10.5 7.5 L16 13 L10.5 18.5" fill="none" stroke="#222" stroke-width="3" stroke-linecap="round" stroke-linejoin="round"/></svg>
  </a>
  <div class="photo" role="img" aria-label="Photo of a smiling professional woman in glasses and a dark business suit"></div>
</section>

</body>
</html>
```